Email Banner (BrindleNotes)

We require an email banner for our email promotions sent to prospect clients. The banner needs to contain the wording BrindleNotes and use the same colour scheme as the logos attached.

This is for B2B professional's so needs to look like a place you would come to read technology articles.

```html
<!DOCTYPE html>
<html lang="en">
<head>
<meta charset="utf-8">
<title>BrindleNotes Email Banner</title>
<link rel="stylesheet" href="https://fonts.googleapis.com/css2?family=Raleway:wght@500&display=swap">
<style>
  :root {
    --page-bg: #e2e2e2;
    --banner-blue: #0a63b0;
    --banner-teal: #0c5566;
    --banner-green: #0a4424;
    --banner-deep: #05301a;
    --ray-teal: #3cc4c0;
    --ray-blue: #2a9ad8;
    --ray-green: #3fc05a;
    --blob-green: #6aad3d;
    --accent-green: #5cbf4a;
    --accent-blue: #1f8fd0;
    --screen-light: #f4f4f4;
    --screen-grey: #c9c9c9;
    --text-white: #ffffff;
  }
  html, body {
    margin: 0;
    padding: 0;
    width: 1200px;
    height: 603px;
    overflow: hidden;
    background: var(--page-bg);
  }
  .canvas {
    width: 1200px;
    height: 603px;
    display: flex;
    align-items: center;
  }
  .email-banner {
    position: relative;
    width: 1200px;
    height: 400px;
    overflow: hidden;
    background: linear-gradient(90deg, var(--banner-blue) 0%, var(--banner-teal) 42%, var(--banner-green) 72%, var(--banner-deep) 100%);
  }
  .banner-art {
    position: absolute;
    inset: 0;
    width: 1200px;
    height: 400px;
  }
  .brand-name {
    position: absolute;
    left: 115px;
    top: 158px;
    margin: 0;
    font-family: "Raleway", sans-serif;
    font-weight: 500;
    font-size: 76px;
    letter-spacing: -1px;
    line-height: 1;
    color: var(--text-white);
  }
</style>
</head>
<body>
<div class="canvas">
  <section class="email-banner">
    <svg class="banner-art" viewBox="0 0 1200 400" aria-hidden="true">
      <defs>
        <linearGradient id="ray-left" x1="0" x2="1" y1="0" y2="0">
          <stop offset="0" stop-color="var(--ray-blue)" stop-opacity="0.75"/>
          <stop offset="1" stop-color="var(--ray-teal)" stop-opacity="0.9"/>
        </linearGradient>
        <linearGradient id="ray-right" x1="1" x2="0" y1="0" y2="0">
          <stop offset="0" stop-color="var(--ray-green)" stop-opacity="0.9"/>
          <stop offset="1" stop-color="var(--ray-green)" stop-opacity="0.2"/>
        </linearGradient>
        <radialGradient id="glow" cx="0.6" cy="0.5" r="0.5">
          <stop offset="0" stop-color="var(--ray-teal)" stop-opacity="0.3"/>
          <stop offset="1" stop-color="var(--ray-teal)" stop-opacity="0"/>
        </radialGradient>
      </defs>
      <rect class="center-glow" width="1200" height="400" fill="url(#glow)"/>
      <g class="light-rays-left" fill="url(#ray-left)">
        <polygon points="0,60 0,100 760,212 760,204" opacity="0.55"/>
        <polygon points="0,130 0,150 760,210 760,206" opacity="0.5"/>
        <polygon points="0,245 0,280 760,212 760,206" opacity="0.6"/>
        <polygon points="0,355 0,375 760,214 760,210" opacity="0.5"/>
        <polygon points="430,0 480,0 760,206 760,202" opacity="0.8"/>
        <polygon points="130,400 170,400 760,214 760,210" opacity="0.45"/>
      </g>
      <g class="light-rays-right" fill="url(#ray-right)">
        <polygon points="1200,95 1200,110 1000,190 1000,186" opacity="0.8"/>
        <polygon points="1200,170 1200,180 1020,205 1020,202"/>
        <polygon points="1200,330 1200,345 1030,240 1030,236" opacity="0.8"/>
        <polygon points="1100,0 1108,0 1020,95 1016,95" opacity="0.7"/>
        <polygon points="1130,400 1150,400 1030,300 1025,300" opacity="0.7"/>
      </g>
      <g class="accent-marks" fill="none" stroke-width="3.5" stroke-linecap="round">
        <circle cx="730" cy="82" r="7.5" stroke="var(--accent-green)"/>
        <circle cx="1062" cy="208" r="7.5" stroke="var(--accent-blue)"/>
        <path d="M1042 50 L1058 66 M1058 50 L1042 66" stroke="var(--accent-green)"/>
        <path d="M705 329 L721 345 M721 329 L705 345" stroke="var(--ray-teal)"/>
      </g>
      <g class="hero-illustration" role="img" aria-label="Illustration of a desktop monitor displaying stacked documents with a magnifying glass, set on a green shape">
        <path d="M730 130 C 760 85, 900 100, 1010 90 C 1110 80, 1120 140, 1060 190 C 1030 215, 1080 300, 1020 340 C 950 375, 820 360, 760 340 C 720 320, 740 250, 715 200 C 700 170, 710 150, 730 130 Z" fill="var(--blob-green)"/>
        <rect x="758" y="55" width="262" height="292" rx="8" fill="var(--screen-light)" opacity="0.9"/>
      </g>
    </svg>
    <h1 class="brand-name">BrindleNotes</h1>
  </section>
</div>
</body>
</html>
```